Apple bag design for elegant new product

We need a packaging design for a 2 lb apple bag. The apple is called a Tidal Morrow. We want a design that pops off the shelf and distinguishes it from all the other apples on display. We want it to appeal to young, high-end shoppers. The apple variety is originally from Japan, so we want the bag to have a Japanese feel, but not too much. The features of the apple is that it is super sweet (the sweetest apple in the market), green, crunchy/snappy, and it's memorable. The market is along the west coast of the United States. This apple is grown on a family farm in a small town called Hood River in Oregon at the base of Mt. Hood. The final design should communicate an exclusive, limited, high quality product that is memorable and sweet. A photo of the apple is attached, and a few bags are attached as references for the package shape.
Updates
Target Market(s)
young, asian, living west coast
Requirements
Must have
- Tidal Morrow (product name)
Nice to have
- apple flower, mt hood,

```html
<!DOCTYPE html>
<html lang="en">
<head>
<meta charset="utf-8">
<title>Tidal Morrow – 2 lb Apple Bag</title>
<link rel="stylesheet" href="https://fonts.googleapis.com/css2?family=Playfair+Display:wght@700&family=Noto+Sans+JP:wght@900&family=Archivo+Black&family=Inter:wght@700;800&display=swap">
<style>
  :root {
    --backdrop: #e0dcdc;
    --bag-green: #4f9a34;
    --bag-green-light: #7cb85a;
    --brand-green: #0f6b3a;
    --tag-green: #5fa04a;
    --window-pale: #ebe8e7;
    --apple-green: #9cc45a;
    --apple-deep: #6ea83a;
    --badge-navy: #1f3a6b;
    --badge-red: #a3262a;
    --white: #ffffff;
  }
  * { margin: 0; padding: 0; box-sizing: border-box; }
  html, body { width: 1200px; height: 1200px; overflow: hidden; }
  body { background: var(--backdrop); position: relative; font-family: "Inter", sans-serif; }

  .bag { position: absolute; left: 120px; top: 40px; width: 960px; height: 1120px; }
  .bag-art { position: absolute; inset: 0; width: 100%; height: 100%; }

  .product-name {
    position: absolute;
    font-family: "Playfair Display", serif;
    font-weight: 700;
    color: var(--brand-green);
    font-size: 132px;
    line-height: 1;
  }
  .product-name--first { left: 190px; top: 360px; }
  .product-name--second { left: 310px; top: 505px; }

  .variety-tag {
    position: absolute; left: 529px; top: 383px; width: 268px; height: 85px;
    background: var(--tag-green); border-radius: 10px;
    display: flex; align-items: center; justify-content: center;
  }
  .variety-tag span {
    display: flex; align-items: center; justify-content: center;
    width: 252px; height: 69px; border: 3px solid var(--white); border-radius: 6px;
    font-family: "Noto Sans JP", sans-serif; font-weight: 900; font-size: 56px;
    color: var(--white); letter-spacing: 2px;
  }

  .weight-seal {
    position: absolute; left: 49px; top: 754px; width: 178px; height: 178px;
    border-radius: 50%; background: var(--bag-green); border: 5px solid var(--white);
    display: flex; align-items: center; justify-content: center;
    font-family: "Inter", sans-serif; font-weight: 800; font-size: 66px; color: var(--white);
  }

  .origin-seal {
    position: absolute; left: 577px; top: 654px; width: 314px; height: 314px;
    border-radius: 50%; background: var(--badge-navy); border: 8px solid var(--badge-red);
    display: flex; flex-direction: column; align-items: center; justify-content: center;
    color: var(--white); line-height: 1; text-align: center;
  }
  .origin-percent { font-family: "Archivo Black", sans-serif; font-size: 50px; }
  .origin-grown { font-family: "Inter", sans-serif; font-weight: 800; font-size: 30px; margin-top: 10px; }
  .origin-country { font-family: "Archivo Black", sans-serif; font-size: 42px; margin-top: 6px; }
  .origin-state {
    font-family: "Inter", sans-serif; font-weight: 800; font-size: 30px;
    margin-top: 16px; padding: 0 10px 5px; border-bottom: 2px solid var(--white);
  }
</style>
</head>
<body>
  <main class="bag">
    <svg class="bag-art" viewBox="348 216 1269 1484" preserveAspectRatio="none">
      <defs>
        <linearGradient id="bagFill" x1="0" y1="0" x2="0" y2="1">
          <stop offset="0" stop-color="var(--bag-green-light)"/>
          <stop offset="1" stop-color="var(--bag-green)"/>
        </linearGradient>
        <radialGradient id="appleFill" cx="0.5" cy="0.6" r="0.6">
          <stop offset="0" stop-color="var(--apple-green)"/>
          <stop offset="0.7" stop-color="var(--apple-deep)"/>
          <stop offset="1" stop-color="var(--window-pale)"/>
        </radialGradient>
      </defs>
      <rect class="bag-body" x="348" y="216" width="1269" height="1484" fill="url(#bagFill)"/>
      <path class="bag-window" d="M348,620 C600,520 700,470 900,465 C1200,460 1450,500 1617,560 L1617,1330 C1400,1420 1100,1560 900,1545 C700,1530 500,1400 348,1290 Z" fill="var(--window-pale)"/>
      <path class="apple-photo" role="img" aria-label="Photo of green apples inside the bag" d="M348,1000 C500,900 600,640 900,640 C1250,640 1450,900 1617,930 L1617,1330 C1400,1420 1100,1560 900,1545 C700,1530 500,1400 348,1290 Z" fill="url(#appleFill)"/>
      <line class="zip-seal" x1="348" y1="595" x2="1617" y2="585" stroke="#c9c4c3" stroke-width="6"/>
      <rect class="handle-cutout" x="750" y="335" width="485" height="137" rx="45" fill="var(--backdrop)"/>
    </svg>

    <h1 class="product-name product-name--first">Tidal</h1>
    <h1 class="product-name product-name--second">Morrow</h1>
    <div class="variety-tag"><span>青りんご</span></div>
    <div class="weight-seal">2lbs</div>

    <div class="origin-seal">
      <p class="origin-percent">100%</p>
      <p class="origin-grown">Grown in</p>
      <p class="origin-country">USA</p>
      <p class="origin-state">Oregon</p>
    </div>
  </main>
</body>
</html>
```